Design 11 slides

I want 11 keynote slides that represent the 'future of design.' Where design is going. It is for a talk about graphic design.
We are open to interpretation. Each slide has a themed headline.
It is mandatory to have the headline, be inventive with typography or design around it, could be photo, illustration or typography. The headline could appear in the middle of the page, and the design happens around it, up to you.
You must supply a 'keynote' program presentation and an unlocked PDF of each page. or just horizontal Hires JPEGs of each slide are fine. or just an unlocked PDF.
-
SLIDE ONE:
Headline: "The Future of Design for $99.00"
-
SLIDE TWO:
Headline: "Rise Past Ordinary: What are we are up against"
6 typographic points to have on the slide
• Conversation overload
• Battling mediocrity
• Era of austerity
• Government support
• Giving it to the crowd
• Digital reshuffle
-
SLIDE THREE:
Headline: "Data never sleeps"
This is about the information overload consumers are experiencing from online and social media information in the marketplace. (Would be great to see you use all the social media icons involved in the design)
-
SLIDE FOUR:
(facts could animate in one after another for maximum of 20 secs) we estimate 4 secs per fact, but animation not essential
"40,000,000
photos uploaded to glimmora everyday
300,000,000
photos uploaded to palvendo everyday
3,800,000,000
Photos ever taken"
4,000,000,000
Things shared on palvendo Every day
72HRS of Video uploaded to zim vela every minute
-
SLIDE FIVE:
144,800,000,000
Emails sent everyday
822,240
Websites created everyday
499,680
Tarnovikle posts published every day
40,000,320
Quonxa posts published everyday
500,000,000
Blips Per day
-
SLIDE SIX:
Headline: "90% of Data was created in the past two years... and counting"
SLIDE SEVEN
Headline: "Faster and Cheaper"
SLIDE EIGHT
Headline: "Rise Past Ordinary™"
Sub header: "Quantity vs Quality"
(this slide is about is quality better than quantity for design concepts choices)
SLIDE NINE:
Headline: "Era of Austerity"
(this slide should illustrate that clients take less risks, today due to the financial Global Crisis)
SLIDE TEN:
Headline: "what is design?"
(this slide should illustrate the Australian people and Government lack of knowledge and support of design. They are more interested in sport)
SLIDE ELEVEN
"Headline "The Digital revolution reshuffle" ( we would like the word revolution crossed out and replaced with reshuffle"
Thank you
Designers
Financial
- A keynote presentation. and a Static PDF VERSION
Slide size: 1920 wide pixels x 1200 pixels
- Creativity

```html
<!DOCTYPE html>
<html lang="en">
<head>
<meta charset="utf-8">
<title>The Future of Design – Slide Set</title>
<link rel="stylesheet" href="https://fonts.googleapis.com/css2?family=Oswald:wght@300;400;500&family=Marcellus&family=Open+Sans:ital,wght@1,400&display=swap">
<style>
  :root{
    --navy:#17466b;
    --navy-line:#3f6a8c;
    --cream:#f4f1ea;
    --red:#e8453c;
    --red-soft:#f3c3bd;
    --grey:#9a9a9a;
    --ink:#2b3f55;
    --white:#ffffff;
  }
  html,body{margin:0;padding:0;}
  body{width:1200px;height:750px;overflow:hidden;background:var(--white);position:relative;font-family:'Oswald',sans-serif;}
  .block{position:absolute;}
  .cream{background:var(--cream);}
  .navy{background:var(--navy);}
  .band-line{position:absolute;top:0;bottom:0;width:1px;background:var(--navy-line);}
  .abs{position:absolute;margin:0;}

  /* slide 1 */
  .title-hero{color:var(--white);font-size:20px;font-weight:400;width:242px;text-align:center;top:38px;left:28px;}

  /* slide 2 */
  .slide-head{color:var(--navy);font-weight:400;line-height:1.15;}
  .threat-list{list-style:none;padding:0;left:352px;top:83px;color:var(--red);font-family:'Oswald',sans-serif;font-size:7px;letter-spacing:.3px;line-height:12.4px;text-transform:uppercase;}
  .threat-list li::before{content:"✓ ";}

  /* stats */
  .stat{position:absolute;display:flex;align-items:flex-start;gap:7px;}
  .stat-icon{width:23px;height:23px;border-radius:4px;display:flex;align-items:center;justify-content:center;flex:none;}
  .stat-num{color:var(--red);font-size:15px;line-height:15px;font-weight:400;}
  .stat-label{color:var(--navy);font-size:7.5px;line-height:9px;}
  .brand-tag{color:var(--white);font-size:5px;line-height:1;font-family:'Oswald',sans-serif;text-align:center;}

  /* slide 3 network */
  .net-node{position:absolute;width:22px;height:22px;border-radius:4px;display:flex;align-items:center;justify-content:center;color:var(--white);font-size:5px;text-align:center;line-height:1;}

  /* slide 6 */
  .data-caption{left:336px;width:229px;text-align:center;}

  /* slide 7 */
  .speed-word{font-family:'Open Sans',sans-serif;font-style:italic;color:var(--red);font-size:22px;letter-spacing:3px;}

  /* slide 9 */
  .era-word{font-family:'Marcellus',serif;width:228px;left:37px;text-align:center;letter-spacing:3px;font-size:17px;line-height:22px;}
</style>
</head>
<body>

<!-- ROW 1 -->
<div class="block cream" style="left:0;top:0;width:28px;height:186px"></div>
<section class="block navy" style="left:28px;top:0;width:242px;height:186px" aria-label="Slide one"></section>
<h1 class="abs title-hero">The Future of Design for</h1>
<svg class="block" style="left:95px;top:70px" width="120" height="100" viewBox="0 0 120 100" aria-label="Price tag $99.00">
  <g transform="rotate(-30 60 50)">
    <path d="M18 32 H88 L106 50 L88 68 H18 Z" fill="var(--red)"/>
    <circle cx="90" cy="50" r="5" fill="var(--navy)"/>
    <text x="50" y="57" text-anchor="middle" fill="var(--white)" font-family="Oswald, sans-serif" font-size="19">$99.00</text>
  </g>
</svg>

<div class="block navy" style="left:300px;top:0;width:36px;height:186px"></div>
<section class="block cream" style="left:336px;top:0;width:229px;height:186px" aria-label="Slide two"></section>
<h2 class="abs slide-head" style="left:339px;top:18px;font-size:17px;">Rise Past Ordinary:<br>What are we are up against</h2>
<ul class="abs threat-list">
  <li>Conversation overload</li>
  <li>Battling mediocrity</li>
  <li>Era of austerity</li>
  <li>Government support</li>
  <li>Giving it to the crowd</li>
  <li>Digital reshuffle</li>
</ul>

<div class="block navy" style="left:565px;top:0;width:71px;height:186px"><span class="band-line" style="left:35px"></span></div>
<section class="block cream" style="left:636px;top:0;width:229px;height:186px" aria-label="Slide three"></section>
<h2 class="abs slide-head" style="left:639px;top:15px;font-size:15px;">Data never sleeps...</h2>
<svg class="block" style="left:636px;top:0" width="229" height="186" viewBox="636 0 229 186">
  <g stroke="#c9c6c0" stroke-width="1">
    <line x1="750" y1="108" x2="700" y2="62"/><line x1="750" y1="108" x2="748" y2="50"/>
    <line x1="750" y1="108" x2="792" y2="67"/><line x1="750" y1="108" x2="807" y2="110"/>
    <line x1="750" y1="108" x2="790" y2="145"/><line x1="750" y1="108" x2="748" y2="170"/>
    <line x1="750" y1="108" x2="704" y2="146"/><line x1="750" y1="108" x2="690" y2="111"/>
  </g>
  <circle cx="750" cy="108" r="18" fill="#b5b3ae" stroke="#8e8c88" stroke-width="2"/>
  <text x="750" y="111" text-anchor="middle" font-family="Oswald, sans-serif" font-size="6" fill="#555">DESIGN</text>
</svg>
<div class="net-node" style="left:689px;top:51px;background:#cf3b34;">Corvella</div>
<div class="net-node" style="left:737px;top:39px;background:#4fb6e6;">Blipster</div>
<div class="net-node" style="left:781px;top:56px;background:#ef8a34;">Scrivane</div>
<div class="net-node" style="left:796px;top:99px;background:#d93a30;">zim vela</div>
<div class="net-node" style="left:781px;top:136px;width:18px;height:18px;background:#e04b3a;">Orbiquo</div>
<div class="net-node" style="left:737px;top:159px;background:#3aa5d8;">Loopera</div>
<div class="net-node" style="left:693px;top:135px;background:#3b5f9c;">palvendo</div>
<div class="net-node" style="left:681px;top:102px;width:18px;height:18px;background:#a8826a;">glimmora</div>

<div class="block navy" style="left:865px;top:0;width:71px;height:186px"><span class="band-line" style="left:35px"></span></div>
<section class="block cream" style="left:936px;top:0;width:264px;height:186px" aria-label="Slide four"></section>
<div class="stat" style="left:964px;top:20px"><span class="stat-icon" style="background:#a8826a"><span class="brand-tag">glimmora</span></span><div><div class="stat-num">40,000,000</div><div class="stat-label">Photos uploaded to glimmora everyday</div></div></div>
<div class="stat" style="left:964px;top:51px"><span class="stat-icon" style="background:#3b5f9c"><span class="brand-tag">palvendo</span></span><div><div class="stat-num">300,000,000</div><div class="stat-label">Photos uploaded to palvendo</div></div></div>
<div class="stat" style="left:964px;top:82px"><span class="stat-icon" style="background:#ef7a30"><svg width="14" height="11" viewBox="0 0 14 11"><rect x="0" y="2" width="14" height="9" rx="1.5" fill="#fff"/><rect x="4" y="0" width="6" height="3" fill="#fff"/><circle cx="7" cy="6.5" r="2.6" fill="#ef7a30"/></svg></span><div><div class="stat-num">3,800,000,000</div><div class="stat-label">Photos ever taken</div></div></div>
<div class="stat" style="left:964px;top:113px"><span class="stat-icon" style="background:#55b948"><svg width="13" height="13" viewBox="0 0 13 13"><g fill="#fff"><circle cx="10" cy="2.5" r="2.2"/><circle cx="2.5" cy="6.5" r="2.2"/><circle cx="10" cy="10.5" r="2.2"/></g><path d="M10 2.5 2.5 6.5 10 10.5" stroke="#fff" stroke-width="1.2" fill="none"/></svg></span><div><div class="stat-num">4,000,000,000</div><div class="stat-label">Things shared on palvendo everyday</div></div></div>
<div class="stat" style="left:964px;top:144px"><span class="stat-icon" style="background:#d93a30"><span class="brand-tag">zim vela</span></span><div><div class="stat-num">72hrs</div><div class="stat-label">of Video uploaded to zim vela every minute</div></div></div>

<!-- ROW 2 -->
<section class="block cream" style="left:0;top:277px;width:265px;height:186px" aria-label="Slide five"></section>
<div class="stat" style="left:44px;top:296px"><span class="stat-icon" style="background:var(--navy)"><svg width="13" height="12" viewBox="0 0 13 12"><path d="M1 6v5h11V6" stroke="#fff" stroke-width="1.6" fill="none"/><path d="M6.5 0v6M4 4l2.5 2.5L9 4" stroke="#fff" stroke-width="1.6" fill="none"/></svg></span><div><div class="stat-num">144,800,000,000</div><div class="stat-label">Emails sent everyday</div></div></div>
<div class="stat" style="left:44px;top:328px"><span class="stat-icon" style="background:var(--navy)"><svg width="12" height="12" viewBox="0 0 12 12"><rect x="1" y="1" width="10" height="10" stroke="#fff" stroke-width="1.4" fill="none"/><path d="M3 4h6M3 6.5h6M3 9h6" stroke="#fff"/></svg></span><div><div class="stat-num">822,240</div><div class="stat-label">Websites created everyday</div></div></div>
<div class="stat" style="left:44px;top:359px"><span class="stat-icon" style="background:var(--navy)"><svg width="12" height="13" viewBox="0 0 12 13"><path d="M1 1h6l3 3v8H1z" stroke="#fff" stroke-width="1.4" fill="none"/><path d="M5.5 6v4M3.5 8h4" stroke="#fff" stroke-width="1.3"/></svg></span><div><div class="stat-num">499,680</div><div class="stat-label">Tarnovikle posts published every day</div></div></div>
<div class="stat" style="left:44px;top:391px"><span class="stat-icon" style="background:var(--navy)"><span class="brand-tag">Quonxa</span></span><div><div class="stat-num">40,000,320</div><div class="stat-label">Quonxa posts published everyday</div></div></div>
<div class="stat" style="left:44px;top:422px"><span class="stat-icon" style="background:var(--navy)"><svg width="14" height="12" viewBox="0 0 14 12"><path d="M1 1h8v5H4l-2 2V6H1z" fill="#fff"/><path d="M10 3h3v5h-1v2l-2-2H6V7h4z" fill="#fff"/></svg></span><div><div class="stat-num">500,000,000</div><div class="stat-label">Blips Per day</div></div></div>

<div class="block navy" style="left:265px;top:277px;width:71px;height:186px"><span class="band-line" style="left:35px"></span></div>
<section class="block cream" style="left:336px;top:277px;width:229px;height:186px" aria-label="Slide six"></section>
<svg class="block" style="left:402px;top:297px" width="96" height="96" viewBox="0 0 96 96" aria-label="Pie chart, 90 percent">
  <circle cx="48" cy="48" r="48" fill="var(--red)"/>
  <path d="M48 48 L48 0 A48 48 0 0 0 19.8 9.2 Z" fill="var(--grey)"/>
  <text x="48" y="63" text-anchor="middle" fill="var(--white)" font-family="Oswald, sans-serif" font-size="40" font-weight="500">90%</text>
</svg>
<p class="abs data-caption" style="top:394px;font-size:7.5px;color:var(--navy);">OF DATA WAS CREATED IN THE</p>
<p class="abs data-caption" style="top:403px;font-size:16px;color:var(--red);">PAST 2 YEARS...</p>
<p class="abs data-caption" style="top:425px;font-size:13px;color:var(--navy);">AND COUNTING</p>

<div class="block navy" style="left:565px;top:277px;width:71px;height:186px"><span class="band-line" style="left:35px"></span></div>
<section class="block cream" style="left:636px;top:277px;width:229px;height:186px" aria-label="Slide seven"></section>
<svg class="block" style="left:683px;top:322px" width="22" height="28" viewBox="0 0 22 28"><path d="M14 0 2 16h8L6 28 20 10h-8z" fill="var(--red)"/></svg>
<p class="abs speed-word" style="left:720px;top:319px;">FASTER</p>
<p class="abs" style="left:746px;top:364px;color:var(--navy);font-size:15px;">AND</p>
<svg class="block" style="left:681px;top:398px" width="26" height="24" viewBox="0 0 26 24"><path d="M1 2h4l3 13h13l3-9H7" stroke="var(--red)" stroke-width="2.4" fill="none"/><circle cx="10" cy="20" r="2.2" fill="var(--red)"/><circle cx="19" cy="20" r="2.2" fill="var(--red)"/></svg>
<p class="abs speed-word" style="left:718px;top:396px;">CHEAPER</p>

<div class="block navy" style="left:865px;top:277px;width:71px;height:186px"><span class="band-line" style="left:35px"></span></div>
<section class="block cream" style="left:936px;top:277px;width:229px;height:186px" aria-label="Slide eight"></section>
<h2 class="abs slide-head" style="left:953px;top:297px;font-size:14px;">Rise Past Ordinary™</h2>
<svg class="block" style="left:936px;top:277px" width="229" height="186" viewBox="936 277 229 186">
  <line x1="963" y1="397" x2="1135" y2="397" stroke="#555" stroke-width="2"/>
  <circle cx="980" cy="376" r="18" fill="var(--grey)"/>
  <text x="980" y="379" text-anchor="middle" fill="var(--white)" font-family="Oswald, sans-serif" font-size="8">Quantity</text>
  <circle cx="1117" cy="386" r="17" fill="var(--red)"/>
  <text x="1117" y="389" text-anchor="middle" fill="var(--white)" font-family="Oswald, sans-serif" font-size="8">Quality</text>
  <text x="1046" y="415" text-anchor="middle" fill="var(--navy)" font-family="Oswald, sans-serif" font-size="13">VS</text>
</svg>
<div class="block navy" style="left:1165px;top:277px;width:35px;height:186px"></div>

<!-- ROW 3 -->
<div class="block navy" style="left:0;top:562px;width:37px;height:188px"></div>
<section class="block cream" style="left:37px;top:562px;width:228px;height:188px" aria-label="Slide nine"></section>
<p class="abs era-word" style="top:578px;color:var(--navy);">ERA</p>
<p class="abs era-word" style="top:600px;color:var(--navy);">OF</p>
<p class="abs era-word" style="top:622px;color:var(--red);">AUSTERITY</p>
<div class="block" role="img" aria-label="Illustration of a family sharing a meagre meal at a table" style="left:85px;top:645px;width:130px;height:80px;background:linear-gradient(135deg,#b7a27a,#8a6b4a 60%,#6e5a45);"></div>

<div class="block navy" style="left:265px;top:562px;width:70px;height:188px"><span class="band-line" style="left:35px"></span></div>
<section class="block cream" style="left:335px;top:562px;width:230px;height:188px" aria-label="Slide ten"></section>
<p class="abs" style="left:335px;width:230px;text-align:center;top:576px;color:var(--red);font-size:28px;line-height:30px;">?</p>
<p class="abs" style="left:335px;width:230px;text-align:center;top:616px;color:var(--red);font-size:8px;">What is design?</p>
<div class="block" role="img" aria-label="Photo of sports fans cheering on a couch" style="left:335px;top:630px;width:230px;height:120px;background:linear-gradient(180deg,rgba(244,241,234,0) 0%,#d8c8b8 30%,#a8423d 65%,#3a3a3a 100%);"></div>

<div class="block navy" style="left:565px;top:562px;width:71px;height:188px"><span class="band-line" style="left:35px"></span></div>
<section class="block cream" style="left:636px;top:562px;width:229px;height:188px" aria-label="Slide eleven"></section>
<svg class="block" style="left:636px;top:562px" width="229" height="188" viewBox="636 562 229 188">
  <path d="M705 642 A50 50 0 1 1 760 710" stroke="var(--red-soft)" stroke-width="15" fill="none"/>
  <path d="M692 630 l26 -2 -8 22 z" fill="var(--red-soft)"/>
  <text x="750" y="643" text-anchor="middle" fill="var(--navy)" font-family="Oswald, sans-serif" font-size="20">The Digital</text>
  <text x="750" y="684" text-anchor="middle" fill="var(--red)" font-family="Oswald, sans-serif" font-size="37">“RESUFFLE”</text>
</svg>
<div class="block navy" style="left:865px;top:562px;width:35px;height:188px"></div>

</body>
</html>
```